Getting things right first Time for Malaysia Citizens - KORVASI

We need a powerful, modern and thought provoking presentation for the Malaysian Government performance unit.
The people will include senior ministers and civil servants, who have all worked in private business.
The website is below
http://www.korvasi.example.my/
The aim is to show by bringing new ways of thinking they can change the way the Malaysian government works, get things right 1st time for customers and work and save tax payers money.
I am presenting why they should work with me as a former Leader (Mayor) of the 4th largest City in the UK. I want to show I am a true moderniser and innovation leader in public sector services.
The presentation will cover new ideas such as citizen co- production, community budgets, and niche marketing for tourism.
For reference my website is
Hello The format is
Slides to be added
Target Market(s)
Minister and senior Civil Servants in Malaysia
Industry/Entity Type
Government
Requirements
Must have
- My Logo and a common set of background.
I will provide some photos but you must provide some from stock on things like holiday destinations in Malaysia, symbols of good public service
About 10 slides in starting with into of me and then specific projects carried out and results.
Will be need to embed a video uploaded from you tube
Nice to have
- Nice to show how modern public services can achieve getting things right for the customer right first time

```html
<!DOCTYPE html>
<html lang="en">
<head>
<meta charset="utf-8">
<title>Key Results in Sheffield</title>
<link href="https://fonts.googleapis.com/css2?family=Carlito:wght@400;700&display=swap" rel="stylesheet">
<style>
  :root {
    --navy: #1f2a5c;
    --ink: #111111;
    --lilac: #e9d9f3;
    --pink: #f0a6df;
    --violet: #a45ac8;
    --deep-violet: #6f2a8f;
    --orange: #f3a43a;
    --frame: #ffffff;
    --bullet: #8a8f9e;
  }
  html, body {
    margin: 0;
    padding: 0;
    width: 1200px;
    height: 899px;
    overflow: hidden;
  }
  .slide {
    position: relative;
    width: 1200px;
    height: 899px;
    overflow: hidden;
    font-family: "Carlito", "Calibri", sans-serif;
    background:
      radial-gradient(ellipse 520px 420px at 560px 380px, rgba(196,170,240,0.35), transparent 70%),
      radial-gradient(ellipse 420px 500px at 60px 560px, rgba(236,200,240,0.55), transparent 70%),
      radial-gradient(ellipse 600px 300px at 700px 820px, rgba(200,150,230,0.45), transparent 70%),
      linear-gradient(180deg, #ffffff 0%, #fbf6fd 55%, var(--lilac) 100%);
  }
  .header-band {
    position: absolute;
    left: 0; top: 0;
    width: 1200px; height: 94px;
    background:
      linear-gradient(90deg, rgba(255,255,255,0.85) 0%, rgba(255,255,255,0.2) 45%, rgba(255,255,255,0) 100%),
      linear-gradient(180deg, #b46fc8 0%, #e7a2dd 60%, #f6d6ef 100%);
    border-bottom: 2px solid rgba(150,90,180,0.5);
  }
  .title {
    position: absolute;
    left: 66px; top: 14px;
    margin: 0;
    font-size: 58px;
    font-weight: 400;
    letter-spacing: -1px;
    color: var(--navy);
    text-shadow: 2px 2px 3px rgba(0,0,0,0.35);
  }
  .results {
    position: absolute;
    left: 98px; top: 180px;
    width: 580px;
    margin: 0; padding: 0;
    list-style: none;
  }
  .results li {
    position: relative;
    padding-left: 42px;
    margin-bottom: 12px;
    font-size: 35px;
    line-height: 43px;
    color: var(--ink);
  }
  .results li::before {
    content: "";
    position: absolute;
    left: 2px; top: 13px;
    width: 16px; height: 16px;
    border-radius: 50%;
    background: radial-gradient(circle at 35% 35%, #ffffff 0%, #c5c9d3 40%, var(--bullet) 100%);
  }
  .photo-frame {
    position: absolute;
    left: 718px; top: 182px;
    width: 412px; height: 527px;
    background: var(--frame);
    transform: rotate(0.8deg);
    box-shadow: 3px 4px 10px rgba(0,0,0,0.35);
  }
  .photo {
    position: absolute;
    left: 12px; top: 22px;
    width: 372px; height: 476px;
    background:
      linear-gradient(180deg, #1b2a6e 0%, #2a3576 30%, #4a3a35 55%, #6e6a5a 80%, #3e4a3a 100%);
  }
  .footer-band {
    position: absolute;
    left: 0; bottom: 0;
    width: 1200px; height: 22px;
    background: linear-gradient(90deg, var(--violet), var(--deep-violet) 50%, var(--violet));
    border-top: 4px solid var(--orange);
  }
  .agency-mark {
    position: absolute;
    left: 930px; top: 815px;
    display: flex;
    align-items: center;
    gap: 12px;
  }
  .agency-mark .dot {
    width: 42px; height: 42px;
    border-radius: 50%;
    background: var(--deep-violet);
  }
  .agency-mark .name {
    font-size: 32px;
    font-weight: 400;
    color: #333333;
    letter-spacing: 1px;
  }
</style>
</head>
<body>
<main class="slide">
  <div class="header-band" role="img" aria-label="City skyline at night in pink and purple tones"></div>
  <h1 class="title">Key Results in Sheffield</h1>

  <ul class="results">
    <li>20% increase in customer satisfaction</li>
    <li>Co production techniques used</li>
    <li>Localism and devolution of services</li>
    <li>Re offending rates down from 34% to 3%</li>
    <li>Niche Tourism developed for the City</li>
    <li>Use of Apps and Crowd Scourcing</li>
  </ul>

  <figure class="photo-frame" style="margin:0">
    <div class="photo" role="img" aria-label="Sheffield Town Hall and illuminated public gardens at dusk"></div>
  </figure>

  <div class="agency-mark">
    <span class="dot"></span>
    <span class="name">KORVASI</span>
  </div>

  <div class="footer-band"></div>
</main>
</body>
</html>
```